New furniture company needs a cool, fresh Website - think lounjo.com, velmora.com

Quiltrest.com: We are launching a home (Shopify) furniture business, aimed at the young, discerning mid-market consumer. The aim is to compete with many furniture e-tailers, as well as more established retail brands.
We want the website to capture the hearts, minds and wallets of the target audience, placing Quiltrest.com firmly into the market place. Please look to Velmora.com for look and feel inspiration. We will be selling approx 15 products to start. I suggest using Shopify with the following theme please: – Hearth & Meadow – Cadenza – Ravel. Please see the logo below. The website needs to have a sophisticated feel for affordable aspirational furniture. Soft colours and homely text - please go with look and feel of Velmora.com. Please see a below file containing image of some sofas, chairs and footstools that will be for sale.
Many thanks

Target Market(s)

mid-market, young families looking for cool, affordable, easy to buy furniture

Industry/Entity Type

Furniture

Coding

Coded - Design and coding required

Number of Pages Required

5+ page

Font styles to use
Sans Serif

Colors
86cae7
cee9f5
3277b5
eaf2ce
fdf9ce
fff3d1
0255a3
e8e8e8
cbcbcb

Requirements
Must have
• Shopify
• http://www.velmora.com/hartwick-leather-large-sofa.html - great example of what we need it to look like
• logo as shown
• homepage
• products menu - sofas, seating, footstools, antique
• images of all products (examples provided) with ability to click on various fabric swatch samples and see the sofa in different fabrics and colours (check out lounjo.com)
• facility for social media
• facility to buy online
• "add to wishlist"
• "add to basket"
Nice to have
• I want it to have a light and airy feel, nothing too heavy or corporate. Needs to be very easily navigated and a simple approach
Should not have
• Dark, heavy colours

```html
<!DOCTYPE html>
<html lang="en">
<head>
<meta charset="utf-8">
<title>Quiltrest — Sofas</title>
<link href="https://fonts.googleapis.com/css2?family=Poppins:wght@300;400;500&display=swap" rel="stylesheet">
<style>
:root{
  --ink:#222;
  --muted:#777;
  --line:#e8e8e8;
  --star:#f0a020;
  --star-off:#d8d8d8;
  --band:#f4f5f7;
  --footer:#f2f3f5;
  --bottom:#4a4e5d;
  --tick:#3a9a3a;
  --white:#fff;
}
*{box-sizing:border-box;margin:0;padding:0}
html,body{width:749px;height:1200px;overflow:hidden;background:var(--white)}
body{font-family:'Poppins',sans-serif;color:var(--ink);position:relative}
.abs{position:absolute}
/* header */
.site-header{position:absolute;left:0;top:0;width:749px;height:50px;background:var(--white)}
.main-nav{position:absolute;left:56px;top:20px;display:flex;gap:17px;font-size:7px;text-transform:uppercase;letter-spacing:.1px}
.main-nav a{color:var(--ink);text-decoration:none}
.main-nav a.active{color:#aaa;border-bottom:1px solid #bbb;padding-bottom:4px}
.brand{position:absolute;left:0;width:749px;top:10px;text-align:center}
.brand-mark{display:block;margin:0 auto 4px;width:14px;height:14px;border:1px solid #999;border-radius:50%}
.brand-name{font-size:8px;letter-spacing:2.5px;color:#888;font-weight:400}
.user-nav{position:absolute;right:56px;top:17px;display:flex;align-items:center;gap:11px;font-size:7px;text-transform:uppercase}
.user-nav span{display:flex;align-items:center;gap:4px}
.cart-count{position:absolute;left:-6px;top:-5px;width:8px;height:8px;border-radius:50%;background:#f4e27a;font-size:5px;text-align:center;line-height:8px}
/* hero */
.hero{position:absolute;left:0;top:50px;width:749px;height:126px;background:linear-gradient(180deg,#f1f1f0 0%,#ececea 70%,#e6e2d6 100%)}
.hero-title{position:absolute;top:38px;width:100%;text-align:center;font-size:21px;font-weight:300}
.breadcrumb{position:absolute;top:74px;width:100%;text-align:center;font-size:8px}
.breadcrumb b{font-weight:400;margin:0 12px}
/* filters */
.filters{position:absolute;left:0;top:176px;width:749px;height:56px;background:var(--band)}
.select{position:absolute;top:15px;height:25px;width:198px;background:var(--white);border:1px solid var(--line);font-size:7px;color:#555;padding:0 10px;display:flex;align-items:center;justify-content:space-between}
.swatch-dot{display:inline-block;width:8px;height:8px;border-radius:50%;background:#ccc;margin-right:6px;vertical-align:middle}
/* products */
.section-rule{position:absolute;left:351px;top:257px;width:47px;height:1px;background:#ccc}
.section-title{position:absolute;top:260px;width:749px;text-align:center;font-size:17px;font-weight:300}
.product{position:absolute;width:154px;height:235px;border:1px solid var(--line);background:var(--white);text-align:center}
.stars{margin-top:20px;font-size:9px;letter-spacing:1px;color:var(--star)}
.stars i{font-style:normal;color:var(--star-off)}
.product-name{font-size:8.5px;margin-top:3px}
.price{font-size:8.5px;color:var(--muted);margin-top:4px}
.product-img{margin:8px auto 0;width:100px;height:98px;border-radius:4px}
.shop-btn{position:absolute;left:35px;bottom:22px;width:83px;height:27px;border:1px solid var(--line);border-radius:14px;font-size:6.5px;color:#666;display:flex;align-items:center;justify-content:center;gap:4px;background:var(--white)}
.shop-btn.hover{border:none;box-shadow:0 2px 8px rgba(0,0,0,.15);color:var(--ink);font-weight:500}
.badge-new{position:absolute;left:28px;top:77px;width:22px;height:22px;border-radius:50%;background:#fbf0c4;font-size:6px;line-height:22px;font-weight:500}
/* services */
.service{position:absolute;top:838px;width:158px;height:98px;border:1px solid var(--line);padding:12px 0 0 22px}
.service-head{display:flex;align-items:flex-end;gap:5px;font-size:10px;color:#333;margin-bottom:9px}
.service-icon{width:14px;height:16px;border-radius:2px}
.service ul{list-style:none;font-size:6px;color:#444;line-height:14px}
.service li::before{content:"\2713";color:var(--tick);margin-right:3px;font-size:7px}
/* footer */
.site-footer{position:absolute;left:0;top:985px;width:749px;height:187px;background:var(--footer)}
.foot-col{position:absolute;top:40px}
.foot-col h4{font-size:11px;font-weight:400;color:#333;margin-bottom:17px}
.foot-col ul{list-style:none;font-size:7.5px;color:#666;line-height:20px}
.foot-col li::before{content:"\203A";margin-right:3px}
.foot-col p{font-size:7.5px;color:#666}
.subscribe{margin-top:9px;width:160px;height:20px;background:var(--white);border-radius:10px;font-size:6.5px;color:#aaa;padding:0 11px;display:flex;align-items:center;justify-content:space-between}
.social{display:flex;gap:10px;margin-top:14px}
.social span{width:6px;height:6px;border-radius:50%;background:#aaa}
.social span.on{background:#333}
.bottom-bar{position:absolute;left:0;top:1172px;width:749px;height:28px;background:var(--bottom);color:#fff;font-size:7.5px;display:flex;align-items:center;justify-content:space-between;padding:0 56px}
</style>
</head>
<body>

<header class="site-header">
  <nav class="main-nav">
    <a href="#">Home</a><a href="#" class="active">Sofas</a><a href="#">Seating</a><a href="#">Footstools</a><a href="#">Antique</a>
  </nav>
  <div class="brand"><span class="brand-mark"></span><span class="brand-name">QUILTREST</span></div>
  <div class="user-nav">
    <span><svg width="13" height="13" viewBox="0 0 24 24"><path d="M12 2l3 7h7l-5.5 4.5 2 7.5-6.5-4-6.5 4 2-7.5L2 9h7z" fill="none" stroke="#999" stroke-width="1.2"/></svg>Wishlist &#8964;</span>
    <span><svg width="15" height="15" viewBox="0 0 24 24"><circle cx="12" cy="12" r="11" fill="none" stroke="#999"/><circle cx="12" cy="9" r="4" fill="none" stroke="#999"/><path d="M5 20c2-4 12-4 14 0" fill="none" stroke="#999"/></svg>Account &#8964;</span>
    <span style="position:relative"><svg width="16" height="14" viewBox="0 0 24 20"><path d="M1 2h4l3 11h12l2-8H7" fill="none" stroke="#999" stroke-width="1.3"/><circle cx="10" cy="17" r="1.5" fill="#999"/><circle cx="18" cy="17" r="1.5" fill="#999"/></svg><em class="cart-count" style="font-style:normal;left:12px">0</em>Cart &#8964;</span>
    <span><svg width="10" height="10" viewBox="0 0 20 20"><circle cx="8" cy="8" r="6" fill="none" stroke="#999" stroke-width="1.6"/><path d="M13 13l5 5" stroke="#999" stroke-width="1.6"/></svg></span>
  </div>
</header>

<section class="hero" role="img" aria-label="Living room with cream sofa, blue armchair and cushions">
  <h1 class="hero-title">Sofas</h1>
  <div class="breadcrumb">Home<b>&#8250;</b>Sofas</div>
</section>

<section class="filters">
  <div class="select" style="left:56px">Select Fabric<span>&#8964;</span></div>
  <div class="select" style="left:276px"><span><span class="swatch-dot"></span>Select Color</span><span>&#8964;</span></div>
  <div class="select" style="left:495px">Rating<span>&#8964;</span></div>
</section>

<div class="section-rule"></div>
<h2 class="section-title">Featured Products</h2>

<article class="product" style="left:56px;top:299px">
  <div class="stars">★★★★<i>★</i></div><div class="product-name">Product name here</div><div class="price">$120.25</div>
  <div class="product-img" role="img" aria-label="Gold velvet armchair" style="background:linear-gradient(#fff,#c9a36a 40%,#8a6a3c)"></div>
  <div class="shop-btn">🛒 SHOP NOW</div>
</article>
<article class="product" style="left:217px;top:299px">
  <div class="stars">★★★★★</div><div class="product-name">Product name here</div><div class="price">$120.25</div>
  <div class="product-img" role="img" aria-label="Cream wingback armchair" style="background:linear-gradient(#fff,#eee6da 40%,#d6ccbc)"></div>
  <div class="shop-btn">🛒 SHOP NOW</div>
</article>
<article class="product" style="left:378px;top:299px">
  <div class="stars">★★★★★</div><div class="product-name">Product name here</div><div class="price">$120.25</div>
  <div class="badge-new">NEW</div>
  <div class="product-img" role="img" aria-label="Black leather chaise longue" style="width:120px;margin-left:30px;background:linear-gradient(#fff,#4a4650 40%,#2a282e)"></div>
  <div class="shop-btn">🛒 SHOP NOW</div>
</article>
<article class="product" style="left:539px;top:299px">
  <div class="stars">★★★★★</div><div class="product-name">Product name here</div><div class="price">$120.25</div>
  <div class="product-img" role="img" aria-label="Purple tufted round footstool" style="width:85px;background:radial-gradient(#4c3a6a,#2c2040 70%,#fff 72%)"></div>
  <div class="shop-btn">🛒 SHOP NOW</div>
</article>

<article class="product" style="left:56px;top:550px">
  <div class="stars">★★★<i>★★</i></div><div class="product-name">Product name here</div><div class="price">$120.25</div>
  <div class="product-img" role="img" aria-label="Cream button-back chair" style="background:linear-gradient(#fff,#e6dcc6 40%,#cfc2a6)"></div>
  <div class="shop-btn">🛒 SHOP NOW</div>
</article>
<article class="product" style="left:217px;top:550px">
  <div role="img" aria-label="Brown sofa with blue cushions in a living room" style="height:165px;background:linear-gradient(180deg,#e7e2d8 0%,#d9d1c6 45%,#6e5048 62%,#8a7a70 78%,#e3ded6 100%)"></div>
  <div class="shop-btn hover">🛒 SHOP NOW</div>
</article>
<article class="product" style="left:378px;top:550px">
  <div class="stars">★★★★★</div><div class="product-name">Product name here</div><div class="price">$120.25</div>
  <div class="product-img" role="img" aria-label="Upholstered bench footstool" style="width:110px;background:linear-gradient(#fff 20%,#cbb49c 40%,#a89a8a)"></div>
  <div class="shop-btn">🛒 SHOP NOW</div>
</article>
<article class="product" style="left:539px;top:550px">
  <div class="stars">★★★★<i>★</i></div><div class="product-name">Product name here</div><div class="price">$120.25</div>
  <div class="product-img" role="img" aria-label="Sage green lounge chair" style="background:linear-gradient(#fff,#8a9a7c 40%,#66745a)"></div>
  <div class="shop-btn">🛒 SHOP NOW</div>
</article>

<div class="service" style="left:56px">
  <div class="service-head"><span class="service-icon" role="img" aria-label="ID badge icon" style="background:#6a8ad0"></span>Business Identity</div>
  <ul><li>Aenean vulputate eleifend tellus.</li><li>Phasellus viverra nulla ut metus.</li><li>Nam quam nunc, blandit vel.</li></ul>
</div>
<div class="service" style="left:216px">
  <div class="service-head"><span class="service-icon" role="img" aria-label="Credit card icon" style="height:9px;background:#e89070"></span>E-Credit line</div>
  <ul><li>Peni sulputate eleifend tellus dolor.</li><li>Asellus viverra nulla ut metus dec.</li><li>Ipsum uam nunc blandi vel lorem.</li></ul>
</div>
<div class="service" style="left:375px">
  <div class="service-head"><span class="service-icon" role="img" aria-label="Inspection document icon" style="width:18px;background:#9ab0c8"></span>Inspection service</div>
  <ul><li>Aenean vulputate eleifend tellus.</li><li>Phasellus viverra nulla ut metus.</li><li>Nam quam nunc, blandit vel.</li></ul>
</div>
<div class="service" style="left:535px">
  <div class="service-head"><span class="service-icon" role="img" aria-label="Globe icon" style="border-radius:50%;height:14px;background:#4aa0d8"></span>Logistics service</div>
  <ul><li>Peni sulputate eleifend tellus dolor.</li><li>Asellus viverra nulla ut metus dec.</li><li>Ipsum uam nunc blandi vel lorem.</li></ul>
</div>

<footer class="site-footer">
  <div class="foot-col" style="left:56px"><h4>How to buy</h4><ul><li>Making Payments</li><li>Delivery Options</li><li>Buyer Protection</li><li>New User Guide</li></ul></div>
  <div class="foot-col" style="left:214px"><h4>Customer Service</h4><ul><li>Customer Service</li><li>Transaction Service Agreement</li><li>Take Our Survey</li><li>Organization &amp; Technical Support</li></ul></div>
  <div class="foot-col" style="left:391px"><h4>Partner Promotion</h4><ul><li>Partnerships</li><li>Affiliate Program</li></ul></div>
  <div class="foot-col" style="left:534px"><h4>Subscribe &amp; Follow</h4><p>Subscribe to our newsletter for latest news.</p>
    <div class="subscribe">Email address...<svg width="8" height="8" viewBox="0 0 20 20"><path d="M1 9l18-8-6 18-3-7z" fill="#999"/></svg></div>
    <div class="social"><span></span><span class="on"></span><span></span><span></span></div>
  </div>
</footer>
<div class="bottom-bar"><span>© 2017,All Rights Reserved.</span><span>Privacy policy &nbsp;&nbsp; · &nbsp;&nbsp; Terms &amp; Conditions</span></div>

</body>
</html>
```